Liquor Label / Aguardiente

Label design for liquor bottle. Designers may submit multiple submissions.

Product Description:
Name: Viento de Plata™
Alcohol Category: Aguardiente (which in Spanish most closely translates to “burning water”) – aguardiente is derived from
cane sugar and is a general term for a type of alcoholic spirit in many Central and South America countries.
Taste: A smooth liquor with a comfortable yet spicy finish
Smell: Subtle aroma of spicy jalapeños
Liquid Color: Clear
Bottle Color: Clear
See link for reference - http://www.kelvostamp.com/sites/default/files/styles/uc_product_full/public/Pemrow_0.jpg?itok=9QmT2xLp
Closure: Bar top / cork
Bottle Shape/Size: height = 8.67in; diameter of base = 3.70in; diameter of neck = 0.85in

Label may consist of two separate parts (i.e. front and back, front and vertical side), or one continuous label.

Designer has complete freedom with color, font etc. unless otherwise stated below. The label MUST
contain (but is not limited only to) the following text exactly as written in quotes below:
- “Viento de Plata”
- “Aguardiente”
- “Cane Neutral Spirit with Natural Flavors”
- “35% Alc./Vol.”
- “750 ml”
- “Bottled by WP Spirits, LLC” and “Nashville, TN” - “Government Warning: (1) According to the Surgeon General, women should not drink alcoholic beverages during
pregnancy because of the risk of birth defects. (2) Consumption of alcoholic beverages impairs your ability to
drive a car or operate machinery, and may cause health problems.” (text in previous quotes must be in all
capitalized letters, text must be 2 MM in height and quote must be separated 2MM by all other text)
- Must be dedicated empty space for bar code (approximately 0.75in. height x 1.25in. length)

Target Market(s)

Label should have mass market appeal.
Age: 21 – 28 years old (primary target market is 21+ year old college students and recent graduates)
Target Market Gender: Both male and female, with emphasis on male
Consumption Focus: Spirit will be consumed typically as a shot, primarily at bars and secondarily off premise (label design will be critical for making our product highly visible behind a bar)
Marketing Theme: South American elements. The official Viento de Plata mascot is a llama and the incorporation and use of a llama somewhere (however large or small) on the bottle is encourage but by no means required.

Industry/Entity Type

Health

Requirements
Should not have
• Elements that may lead a potential consumer to believe the beverage is a craft liquor or an artisan brand. Please do not include images of peppers.

```html
<!DOCTYPE html>
<html lang="en">
<head>
<meta charset="utf-8">
<title>Viento de Plata — Aguardiente Label Variants</title>
<link rel="stylesheet" href="https://fonts.googleapis.com/css2?family=Bebas+Neue&family=Oswald:wght@400;500&family=Kaushan+Script&display=swap">
<style>
  :root {
    --backdrop: #eeeeef;
    --label-black: #0b0b0b;
    --brand-white: #ffffff;
    --script-blue: #8fc6ea;
    --accent-red: #e2231a;
    --gold-light: #f3dfa2;
    --gold-mid: #c9a24a;
    --gold-dark: #8a6a22;
    --scene-sky: #8cc2e8;
    --scene-hills: #6f9a4a;
    --scene-village: #d9cdb8;
    --fine-print: #c4c4c4;
    --barcode-field: #ffffff;
  }
  * { margin: 0; padding: 0; box-sizing: border-box; }
  html, body { width: 1200px; height: 1089px; overflow: hidden; }
  body {
    background: radial-gradient(ellipse at 50% 40%, #fafafa 0%, var(--backdrop) 70%, #e2e2e4 100%);
    position: relative;
    font-family: "Oswald", sans-serif;
  }
  .label {
    position: absolute;
    top: 390px;
    width: 215px;
    height: 485px;
    background: var(--label-black);
    color: var(--brand-white);
    box-shadow: 0 6px 18px rgba(0,0,0,0.18);
  }
  .label--round { left: 200px; }
  .label--band  { left: 791px; }

  .brand-mark {
    position: absolute;
    top: 10px;
    left: 50%;
    width: 30px;
    height: 30px;
    margin-left: -15px;
    border-radius: 50%;
    background: var(--accent-red);
  }
  .brand-name {
    position: absolute;
    top: 46px;
    left: 0;
    width: 100%;
    text-align: center;
    font-family: "Bebas Neue", sans-serif;
    font-weight: 400;
    color: var(--brand-white);
    line-height: 0.92;
  }
  .brand-name__small { display: block; font-size: 18px; letter-spacing: 3px; }
  .brand-name__large { display: block; font-size: 54px; letter-spacing: 1px; }
  .category {
    position: absolute;
    top: 132px;
    left: 0;
    width: 100%;
    text-align: center;
    font-family: "Kaushan Script", cursive;
    font-size: 21px;
    line-height: 26px;
    color: var(--script-blue);
  }
  .spirit-type {
    position: absolute;
    top: 161px;
    left: 0;
    width: 100%;
    text-align: center;
    font-size: 7.5px;
    line-height: 10px;
    letter-spacing: 0.3px;
    text-transform: uppercase;
    color: var(--brand-white);
  }

  .scene {
    position: absolute;
    background: linear-gradient(180deg, var(--scene-sky) 0%, #cfe6f4 38%, var(--scene-hills) 62%, var(--scene-village) 100%);
  }
  .scene--round {
    top: 186px;
    left: 11px;
    width: 193px;
    height: 193px;
    border-radius: 50%;
    border: 4px solid var(--gold-mid);
    box-shadow: 0 0 0 1px var(--gold-light) inset;
  }
  .scene--band {
    top: 183px;
    left: 0;
    width: 215px;
    height: 196px;
  }
  .gold-rule {
    position: absolute;
    left: 0;
    width: 215px;
    height: 5px;
    background: linear-gradient(90deg, var(--gold-dark), var(--gold-light) 35%, var(--gold-mid) 60%, var(--gold-light) 80%, var(--gold-dark));
  }
  .gold-rule--top { top: 178px; }
  .gold-rule--bottom { top: 379px; }

  .details {
    position: absolute;
    top: 392px;
    left: 8px;
    width: 132px;
    text-align: center;
    font-size: 11px;
    line-height: 15px;
    letter-spacing: 0.2px;
    text-transform: uppercase;
  }
  .barcode-space {
    position: absolute;
    top: 394px;
    right: 8px;
    width: 60px;
    height: 40px;
    background: var(--barcode-field);
  }
  .warning {
    position: absolute;
    top: 446px;
    left: 9px;
    width: 197px;
    text-align: center;
    font-size: 5px;
    line-height: 6.4px;
    color: var(--fine-print);
    text-transform: uppercase;
  }
</style>
</head>
<body>

  <section class="label label--round">
    <span class="brand-mark"></span>
    <h1 class="brand-name"><span class="brand-name__small">Viento de</span><span class="brand-name__large">Plata</span></h1>
    <p class="category">Aguardiente</p>
    <p class="spirit-type">Cane Neutral Spirit with Natural Flavors</p>
    <div class="scene scene--round" role="img" aria-label="Photograph of a colonial village street with white houses and tiled roofs beneath green hills and a sunlit sky"></div>
    <div class="details">
      <p>35% Alc./Vol. 750 ml</p>
      <p>Bottled by WP Spirits, LLC</p>
      <p>Nashville, TN</p>
    </div>
    <div class="barcode-space" aria-label="Reserved space for barcode"></div>
    <p class="warning">Government Warning: (1) According to the Surgeon General, women should not drink alcoholic beverages during pregnancy because of the risk of birth defects. (2) Consumption of alcoholic beverages impairs your ability to drive a car or operate machinery, and may cause health problems.</p>
  </section>

  <section class="label label--band">
    <span class="brand-mark"></span>
    <h1 class="brand-name"><span class="brand-name__small">Viento de</span><span class="brand-name__large">Plata</span></h1>
    <p class="category">Aguardiente</p>
    <p class="spirit-type">Cane Neutral Spirit with Natural Flavors</p>
    <span class="gold-rule gold-rule--top"></span>
    <div class="scene scene--band" role="img" aria-label="Photograph of a colonial village street with white houses and tiled roofs beneath green hills and a sunlit sky"></div>
    <span class="gold-rule gold-rule--bottom"></span>
    <div class="details">
      <p>35% Alc./Vol. 750 ml</p>
      <p>Bottled by WP Spirits, LLC</p>
      <p>Nashville, TN</p>
    </div>
    <div class="barcode-space" aria-label="Reserved space for barcode"></div>
    <p class="warning">Government Warning: (1) According to the Surgeon General, women should not drink alcoholic beverages during pregnancy because of the risk of birth defects. (2) Consumption of alcoholic beverages impairs your ability to drive a car or operate machinery, and may cause health problems.</p>
  </section>

</body>
</html>
```